Accounting / taxation / finance frim needs a half size banner. It ll be an advantage if you desing f

We need a half a size (234 x 60) vertical stand banner design for our company based in Melbourne Australia.
We provide range of accounting, taxation services.
We also have strategic alliance with other law firm, migration firm and finance mortgage brokers.
The idea is to create a fully integrated service (one stop shop) for our clients.

We would like to see designs that match our existing website, brochure, business card, letter head and logo.

Our website is www.tormelgroup.com.au... you may get all your contents from this website.

Our business name is Tormel Group. So the final design should deliver the message that we are Group of professionals that work hand in hand with our clients to achieve and go beyond clients need. The design should also convey the message that we are one stop shop to assist clients with their various needs.

Colors
3277b5
85acd3
886aae
b8a6cd
33b8a4
87d0c7
33a6d7
85cae6

Requirements
Must have
• Tormel Group Where planning goes further
• TRML Logo
• BFQ Logo
• Levy Adviser Council Logo
• OWN Logo

```html
<!DOCTYPE html>
<html lang="en">
<head>
<meta charset="utf-8">
<title>TRML 234x60 Animated Banner Frames</title>
<link rel="stylesheet" href="https://fonts.googleapis.com/css2?family=Arimo:wght@400;700&display=swap">
<style>
  :root {
    --navy: #0d3a78;
    --label: #1d4f8c;
    --deep-blue: #0a3d8f;
    --mid-blue: #1f6fc4;
    --sky-blue: #3f8fd8;
    --panel-light: #ffffff;
    --panel-shade: #c8d5e6;
    --frame-edge: #1b1b1b;
    --teal: #1fae97;
    --alert-red: #e8141b;
    --page: #ffffff;
  }
  * { box-sizing: border-box; margin: 0; padding: 0; }
  html, body { width: 1200px; height: 1200px; overflow: hidden; background: var(--page); }
  body { font-family: "Arimo", Arial, sans-serif; position: relative; }

  .frame-row { position: absolute; left: 0; width: 1200px; height: 85px; }
  .frame-label {
    position: absolute; left: 236px; top: 50%; transform: translateY(-50%);
    font-size: 32px; color: var(--label); letter-spacing: 0.5px;
  }
  .banner {
    position: absolute; left: 432px; top: 0; width: 330px; height: 85px;
    border: 1.5px solid var(--frame-edge); overflow: hidden;
    background: linear-gradient(100deg, var(--panel-light) 35%, var(--panel-shade) 100%);
  }
  .banner-swoosh { position: absolute; left: 0; top: 0; width: 130px; height: 85px; }
  .brand {
    position: absolute; left: 14px; top: 6px; width: 80px; height: 76px;
    display: flex; flex-direction: column; align-items: center;
  }
  .brand-mark {
    width: 48px; height: 48px; border-radius: 50%;
    border: 2px solid #bcd6f2; background: var(--mid-blue);
  }
  .brand-name {
    margin-top: 3px; padding: 1px 4px; background: #ffffff;
    font-size: 12px; font-weight: 700; color: var(--navy); line-height: 1.1;
  }
  .banner-copy {
    position: absolute; left: 128px; right: 8px; top: 50%; transform: translateY(-50%);
    font-size: 22px; font-weight: 700; color: var(--navy); line-height: 1.05;
  }
  .banner-copy.is-wide { left: 108px; }
  .banner-copy.is-large { font-size: 30px; text-align: center; left: 110px; }
  .banner-copy.is-tagline { left: 104px; font-size: 18px; line-height: 1.3; }
  .read-more {
    display: inline-block; margin-left: 10px; vertical-align: middle;
    padding: 7px 12px; border-radius: 4px; background: var(--teal);
    color: #ffffff; font-size: 12px; font-weight: 700;
  }

  .sheet-note { position: absolute; left: 0; width: 1200px; text-align: center; }
  .sheet-note.is-status { top: 1062px; font-size: 32px; font-weight: 700; color: var(--alert-red); }
  .sheet-note.is-title { top: 1114px; font-size: 31px; color: var(--navy); }
</style>
</head>
<body>

<svg width="0" height="0" style="position:absolute">
  <defs>
    <linearGradient id="swooshFill" x1="0" y1="0" x2="1" y2="1">
      <stop offset="0" stop-color="#0a3d8f"/>
      <stop offset="1" stop-color="#1f6fc4"/>
    </linearGradient>
    <linearGradient id="swooshGlow" x1="0" y1="0" x2="1" y2="0">
      <stop offset="0" stop-color="#3f8fd8"/>
      <stop offset="1" stop-color="#8cc0ee"/>
    </linearGradient>
    <symbol id="swoosh" viewBox="0 0 130 85">
      <path d="M0 0 H125 C95 10 90 40 92 85 H0 Z" fill="url(#swooshGlow)"/>
      <path d="M0 0 H100 C78 14 76 45 80 85 H0 Z" fill="url(#swooshFill)"/>
      <rect x="0" y="0" width="12" height="85" fill="#062a66"/>
    </symbol>
  </defs>
</svg>

<div class="frame-row" style="top:47px">
  <div class="frame-label">FRAME A</div>
  <div class="banner">
    <svg class="banner-swoosh"><use href="#swoosh"/></svg>
    <div class="brand"><div class="brand-mark"></div><div class="brand-name">TRML</div></div>
    <div class="banner-copy">Bookkeping &amp;<br>Payroll</div>
  </div>
</div>

<div class="frame-row" style="top:150px">
  <div class="frame-label">FRAME B</div>
  <div class="banner">
    <svg class="banner-swoosh"><use href="#swoosh"/></svg>
    <div class="brand"><div class="brand-mark"></div><div class="brand-name">TRML</div></div>
    <div class="banner-copy is-wide">Business Service<br>&amp; Adversory</div>
  </div>
</div>

<div class="frame-row" style="top:253px">
  <div class="frame-label">FRAME C</div>
  <div class="banner">
    <svg class="banner-swoosh"><use href="#swoosh"/></svg>
    <div class="brand"><div class="brand-mark"></div><div class="brand-name">TRML</div></div>
    <div class="banner-copy is-large">Migration</div>
  </div>
</div>

<div class="frame-row" style="top:357px">
  <div class="frame-label">FRAME D</div>
  <div class="banner">
    <svg class="banner-swoosh"><use href="#swoosh"/></svg>
    <div class="brand"><div class="brand-mark"></div><div class="brand-name">TRML</div></div>
    <div class="banner-copy">Taxation,<br>Accounting &amp;<br>Compliances</div>
  </div>
</div>

<div class="frame-row" style="top:466px">
  <div class="frame-label">FRAME E</div>
  <div class="banner">
    <svg class="banner-swoosh"><use href="#swoosh"/></svg>
    <div class="brand"><div class="brand-mark"></div><div class="brand-name">TRML</div></div>
    <div class="banner-copy is-wide">ASIC &amp; Corporate<br>Secretarial</div>
  </div>
</div>

<div class="frame-row" style="top:572px">
  <div class="frame-label">FRAME F</div>
  <div class="banner">
    <svg class="banner-swoosh"><use href="#swoosh"/></svg>
    <div class="brand"><div class="brand-mark"></div><div class="brand-name">TRML</div></div>
    <div class="banner-copy is-wide">Finance &amp; Capital<br>Raising</div>
  </div>
</div>

<div class="frame-row" style="top:685px">
  <div class="frame-label">FRAME G</div>
  <div class="banner">
    <svg class="banner-swoosh"><use href="#swoosh"/></svg>
    <div class="brand"><div class="brand-mark"></div><div class="brand-name">TRML</div></div>
    <div class="banner-copy">Management<br>Consulting<br>Services</div>
  </div>
</div>

<div class="frame-row" style="top:796px">
  <div class="frame-label">FRAME H</div>
  <div class="banner">
    <svg class="banner-swoosh"><use href="#swoosh"/></svg>
    <div class="brand"><div class="brand-mark"></div><div class="brand-name">TRML</div></div>
    <div class="banner-copy">Insulvency &amp;<br>Restructuring</div>
  </div>
</div>

<div class="frame-row" style="top:906px">
  <div class="frame-label">FRAME I</div>
  <div class="banner">
    <svg class="banner-swoosh"><use href="#swoosh"/></svg>
    <div class="brand"><div class="brand-mark"></div><div class="brand-name">TRML</div></div>
    <div class="banner-copy is-tagline">WHERE PLANNING GOES<br>FURTHER<span class="read-more">Read more</span></div>
  </div>
</div>

<div class="sheet-note is-status">ANIMATED</div>
<div class="sheet-note is-title">234X60 TRML Banner ADS</div>

</body>
</html>
```